Contemporary new French wine brand needs logo and series of label design

to design a new contemporary logo and series of labels for a new French wine brand. We hope to attract not just current French wine drinkers but new ones who may appreciate a less traditional and more modern style.
Updates

Reason: we are wanting to extend the project for a few days more to receive more submissions since we had fewer designs submitted than we were expecting, maybe because of the holidays.

Target Market(s)

people who follow the arts community (eg. music, theatre, visual/video arts, dance) --- all mature ages.

Industry/Entity Type

French Wine

Requirements
Must have
• a clear, memorable treatment for the name CLAVINE with accompanying logo.
Nice to have
• embossing, matte/gloss refinement, tasteful foil stamping, coated stock for the whites to help the integrity of the paper in and out of ice buckets. A combo of say, three types of fonts; a semi custom font for the brand name Clavine and maybe a script and one other.
Should not have
• not traditional French

```html
<!DOCTYPE html>
<html lang="en">
<head>
<meta charset="utf-8">
<title>Clavine – Cabernet Sauvignon 2015 label</title>
<link rel="stylesheet" href="https://fonts.googleapis.com/css2?family=Cinzel:wght@400;600&family=Great+Vibes&display=swap">
<style>
  :root {
    --backdrop: #e4e2e2;
    --paper: #f4f4f5;
    --paper-shade: #dcdde0;
    --navy: #1d2e6e;
    --navy-deep: #14214f;
    --ink: #1b1b24;
    --script-tint: #b3bad3;
    --rule-grey: #b9b9be;
  }
  * { margin: 0; padding: 0; box-sizing: border-box; }
  html, body {
    width: 830px;
    height: 1200px;
    overflow: hidden;
    background: var(--backdrop);
  }
  .canvas {
    position: relative;
    width: 830px;
    height: 1200px;
  }
  .label {
    position: absolute;
    left: 40px;
    top: 124px;
    width: 750px;
    height: 952px;
    background: linear-gradient(90deg, var(--paper-shade) 0%, var(--paper) 18%, #ffffff 50%, var(--paper) 82%, var(--paper-shade) 100%);
    border-top: 10px solid var(--navy);
    border-bottom: 6px solid var(--rule-grey);
  }
  .brand-seal {
    position: absolute;
    left: 50%;
    top: -100px;
    width: 350px;
    height: 350px;
    margin-left: -175px;
    border-radius: 50%;
    background: var(--navy);
    display: flex;
    align-items: center;
    justify-content: center;
  }
  .brand-seal__name {
    font-family: "Cinzel", serif;
    font-weight: 400;
    font-size: 46px;
    letter-spacing: 4px;
    color: #ffffff;
  }
  .brand-name {
    position: absolute;
    left: 0;
    right: 0;
    top: 342px;
    text-align: center;
    font-family: "Cinzel", serif;
    font-weight: 400;
    font-size: 78px;
    letter-spacing: 2px;
    color: var(--ink);
  }
  .varietal {
    position: absolute;
    left: 0;
    right: 0;
    top: 578px;
    text-align: center;
    font-family: "Cinzel", serif;
    font-weight: 400;
    font-size: 36px;
    letter-spacing: 3px;
    color: var(--navy);
  }
  .divider {
    position: absolute;
    left: 81px;
    top: 644px;
    width: 588px;
    height: 40px;
  }
  .vintage {
    position: absolute;
    left: 0;
    right: 0;
    top: 704px;
    text-align: center;
    font-family: "Cinzel", serif;
    font-size: 40px;
    letter-spacing: 4px;
    color: var(--navy);
  }
  .rule-thin {
    position: absolute;
    left: 0;
    right: 0;
    top: 782px;
    height: 12px;
    background: var(--navy-deep);
  }
  .origin-band {
    position: absolute;
    left: 0;
    right: 0;
    top: 816px;
    height: 98px;
    background: var(--navy);
    display: flex;
    align-items: center;
    justify-content: center;
  }
  .origin-band__text {
    font-family: "Great Vibes", cursive;
    font-size: 44px;
    color: var(--script-tint);
  }
</style>
</head>
<body>
  <main class="canvas">
    <section class="label">
      <div class="brand-seal">
        <span class="brand-seal__name">CLAVINE</span>
      </div>

      <h1 class="brand-name">CLAVINE</h1>

      <p class="varietal">CABERNET SAUVIGNON</p>

      <svg class="divider" viewBox="0 0 588 40" aria-hidden="true">
        <defs>
          <linearGradient id="divider-fade" x1="0" x2="1" y1="0" y2="0">
            <stop offset="0" stop-color="#1d2e6e" stop-opacity="0"/>
            <stop offset="0.5" stop-color="#1d2e6e"/>
            <stop offset="1" stop-color="#1d2e6e" stop-opacity="0"/>
          </linearGradient>
        </defs>
        <rect x="0" y="18" width="588" height="4" fill="url(#divider-fade)"/>
        <rect role="img" aria-label="small knot ornament" x="244" y="8" width="100" height="24" rx="12" fill="#1d2e6e"/>
      </svg>

      <p class="vintage">2015</p>

      <div class="rule-thin"></div>

      <div class="origin-band">
        <span class="origin-band__text">Product of France</span>
      </div>
    </section>
  </main>
</body>
</html>
```